PRK website

Im a Specialty contractor that specializes in fireproofing. Epoxy flooring and terrazo along with poured floors and polished concrete.

We also do fire caulking.

Im the largest specialty flooring healthcare contractor in the south east.

Otto

Contractor

```html
<!DOCTYPE html>
<html lang="en">
<head>
<meta charset="utf-8">
<title>PRK Fireproofing</title>
<link rel="stylesheet" href="https://fonts.googleapis.com/css2?family=Arimo:ital,wght@0,400;0,700;1,700&family=Roboto+Condensed:wght@700;800&display=swap">
<style>
:root{
  --bg:#222222;
  --panel:#1b1b1b;
  --panel-edge:#333333;
  --nav:#2a2a2a;
  --text:#ffffff;
  --muted:#cfcfcf;
  --dim:#9a9a9a;
  --accent:#f0a35e;
  --red:#c8401a;
  --card:#ffffff;
  --ink:#333333;
}
*{margin:0;padding:0;box-sizing:border-box}
html,body{width:947px;height:1200px;overflow:hidden;background:var(--bg);font-family:Arimo,Arial,sans-serif;color:var(--text)}
.page{position:relative;width:947px;height:1200px}
.abs{position:absolute}

.brand{left:60px;top:24px;display:flex;align-items:baseline;gap:18px;font-weight:700;letter-spacing:-.5px}
.brand .mark{font-size:48px}
.brand .word{font-size:31px;letter-spacing:.5px}
.contact-head{right:60px;top:24px;text-align:right}
.contact-head .phone{font-size:27px;font-weight:700;display:flex;align-items:center;gap:10px;justify-content:flex-end}
.contact-head .addr{font-size:13px;font-weight:700;margin-top:2px}

.nav{left:37px;top:94px;width:871px;height:75px;display:flex;border:1px solid #3a3a3a;background:linear-gradient(#2e2e2e,#1d1d1d)}
.nav a{display:flex;align-items:center;justify-content:center;color:var(--text);text-decoration:none;font-size:13px;font-weight:700;letter-spacing:.6px;border-right:1px solid #3e3e3e;height:100%}
.nav a:last-child{border-right:0}

.hero{left:37px;top:189px;width:873px;height:297px;border-radius:26px;background:var(--panel);border:1px solid var(--panel-edge)}
.hero-card{left:20px;top:19px;width:416px;height:260px;background:var(--card);border-radius:6px 0 0 6px;color:var(--ink);padding:26px 0 0 57px}
.hero-card h1{font-size:23px;font-weight:700;color:#b3b3b3;letter-spacing:0}
.hero-card h1 span{color:#444}
.hero-card .kicker{font-size:10.5px;font-style:italic;font-weight:700;color:var(--red);letter-spacing:.6px;margin-top:2px}
.hero-card p{font-size:13.5px;line-height:21.5px;margin-top:18px;width:310px;color:#333}
.hero-card .more{font-size:12.5px;font-weight:700;margin-top:15px;display:flex;align-items:center;gap:6px}
.hero-photo{left:444px;top:19px;width:409px;height:260px;border-radius:0 6px 6px 0;background:linear-gradient(180deg,#8e9aa2 0%,#a9b0ad 38%,#b09a73 62%,#6e5c45 100%)}

.feature{top:523px;width:290px;height:84px}
.feature .thumb{position:absolute;left:0;top:0;width:84px;height:84px;border-radius:8px;background:#2e2e2e;padding:4px}
.feature .thumb div{width:100%;height:100%;border-radius:6px;background:radial-gradient(circle at 40% 40%,#d9674b,#9a3a24)}
.feature h3{position:absolute;left:98px;top:0;font-size:17px;font-weight:400}
.feature .sub{position:absolute;left:98px;top:21px;font-size:12.5px;font-style:italic;font-weight:700;color:var(--muted)}
.feature p{position:absolute;left:98px;top:39px;font-size:12.5px;line-height:14.5px}
.feature .link{position:absolute;left:98px;top:70px;font-size:11px;color:#333}
.f2 p,.f3 p{color:var(--dim)}

.rule{left:37px;top:634px;width:873px;height:1px;background:#3a3a3a}

.col{top:655px;width:270px}
.col h2{font-family:"Roboto Condensed",Arial Narrow,sans-serif;font-weight:800;font-size:20px;letter-spacing:-.2px}
.col .lead{font-size:14.5px;font-weight:700;line-height:19px;margin-top:14px}
.col p{font-size:14px;line-height:18.5px;margin-top:10px;color:#eee}
.col ul{list-style:none;margin-top:14px}
.col li{font-size:14.5px;font-weight:700;color:var(--accent);line-height:24px;display:flex;align-items:center;gap:10px}
.col li::before{content:"";width:9px;height:9px;border-radius:50%;background:radial-gradient(circle at 35% 35%,#aaa,#555)}

.footer{left:37px;top:865px;width:871px;height:315px;background:var(--panel);border:1px solid #2e2e2e}
.office{top:28px;width:190px}
.office h4,.footer h4{font-size:17px;font-weight:700}
.office p{font-size:13.5px;line-height:22.3px;margin-top:10px;letter-spacing:.2px}
.form{left:632px;top:28px}
.form input,.form textarea{display:block;width:149px;height:20px;border:0;background:linear-gradient(#fff,#e9e9e9);font:12px Arimo,Arial,sans-serif;color:#aaa;padding:2px 5px}
.form textarea{width:204px;height:111px;resize:none;background:linear-gradient(#e6e6e6,#fff 50%)}
.form .send{width:66px;height:26px;margin-top:10px;background:linear-gradient(#fafafa,#cfcfcf);color:#333;font-size:13px;font-weight:700;display:flex;align-items:center;justify-content:center;border-radius:2px}
.badges{top:1109px;display:flex;gap:10px}
.badge{height:38px;border-radius:3px;display:flex;align-items:center;justify-content:center;font-size:11.5px;font-weight:700;padding:0 6px}
.b-light{background:#f4f4f4;color:#1b3d8f}
.b-dark{background:#1a4d8f;color:#fff}
.social{display:flex;gap:9px;top:1109px;left:463px}
.social .s{width:36px;height:38px;border-radius:6px;background:#3b3b3b;display:flex;align-items:center;justify-content:center;font-size:10px;font-weight:700;color:#fff}
</style>
</head>
<body>
<div class="page">

  <header>
    <div class="abs brand"><span class="mark">PRK</span><span class="word">FIREPROOFING</span></div>
    <div class="abs contact-head">
      <div class="phone">
        <svg width="24" height="24" viewBox="0 0 24 24" aria-hidden="true"><path d="M6 20c-3-3-3-10 3-15l3 4c-3 2-3 5-1 7l-2 4z M15 3l4-1 1 4-4 1z" fill="#fff"/></svg>
        (200) 555-0187
      </div>
      <div class="addr">3577 Street, City, ZIP</div>
    </div>
    <nav class="abs nav">
      <a style="width:86px">HOME</a>
      <a style="width:151px">FIREPROOFING</a>
      <a style="width:89px">EPOXY</a>
      <a style="width:105px">TERRAZO</a>
      <a style="width:156px">POURED FLOORS</a>
      <a style="width:186px">POLISHED CONCRETE</a>
      <a style="width:98px">CONTACT</a>
    </nav>
  </header>

  <section class="abs hero">
    <div class="abs hero-card">
      <h1>OMNES<span>VERO</span></h1>
      <div class="kicker">LEGERE CUM FORTE</div>
      <p>Ne audiam ocurreret constituam eam, ea sumo referrentur eum, ea sit nostro nostrum. Pri vidit percipit cotidieque ea, per omittam necessitatibus no, id per audire aliquando. Ei modo minimum erroribus quo, eos ei erat laudem omittam. Solum gloriatur ei usu. Sonet ludus bonorum ea ius, an</p>
      <div class="more">Read more
        <svg width="12" height="10" viewBox="0 0 12 10" aria-hidden="true"><path d="M1 1l4 4-4 4M6 1l4 4-4 4" stroke="#333" stroke-width="1.8" fill="none"/></svg>
      </div>
    </div>
    <div class="abs hero-photo" role="img" aria-label="Bright building lobby with glass walls and a polished stone floor"></div>
  </section>

  <section>
    <div class="abs feature f1" style="left:37px">
      <div class="thumb"><div role="img" aria-label="Red textured floor finish sample"></div></div>
      <h3>Ea per latine partiendo</h3>
      <div class="sub">Ea per latine partiendo</div>
      <p>Sanctus scaevola disputando<br>mea et. Vel vidit audiam</p>
      <div class="link">Read more</div>
    </div>
    <div class="abs feature f2" style="left:328px">
      <div class="thumb"><div role="img" aria-label="Red textured floor finish sample"></div></div>
      <h3>Ea per latine partiendo</h3>
      <div class="sub">Ea per latine partiendo</div>
      <p>Sanctus scaevola disputando<br>mea et. Vel vidit audiam</p>
      <div class="link">Read more</div>
    </div>
    <div class="abs feature f3" style="left:619px">
      <div class="thumb"><div role="img" aria-label="Red textured floor finish sample"></div></div>
      <h3>Ea per latine partiendo</h3>
      <div class="sub">Ea per latine partiendo</div>
      <p>Sanctus scaevola disputando<br>mea et. Vel vidit audiam</p>
      <div class="link">Read more</div>
    </div>
  </section>

  <div class="abs rule"></div>

  <section>
    <div class="abs col" style="left:38px">
      <h2>Per esse magna exerci</h2>
      <div class="lead">In bonorum laboramus pri, in congue animal dissentiet sed. Eu cum harum</div>
      <p>Ne audiam ocurreret constituam eam, ea sumo referrentur eum, ea sit nostro nostrum. Pri vidit percipit cotidieque ea, per omittam necessitatibus no, id per audire aliquando. Ei modo minimum erroribus quo,</p>
    </div>
    <div class="abs col" style="left:329px">
      <h2>Per esse magna exerci</h2>
      <div class="lead">In bonorum laboramus pri, in congue animal dissentiet sed. Eu cum harum</div>
      <p>Ne audiam ocurreret constituam eam, ea sumo referrentur eum, ea sit nostro nostrum. Pri vidit percipit cotidieque ea, per omittam necessitatibus no, id per audire aliquando. Ei modo minimum erroribus</p>
    </div>
    <div class="abs col" style="left:619px">
      <h2>Per esse magna exerci</h2>
      <ul>
        <li>Quot illud cum ut, ut liber iusto</li>
        <li>Quot illud cum ut, ut liber iusto</li>
        <li>Quot illud cum ut, ut liber iusto</li>
        <li>Quot illud cum ut, ut liber iusto</li>
        <li>Quot illud cum ut, ut liber iusto</li>
        <li>Quot illud cum ut, ut liber iusto</li>
      </ul>
    </div>
  </section>

  <footer class="abs footer">
    <div class="abs office" style="left:36px">
      <h4>Iriure Invidunt</h4>
      <p>2121 Sample Avenue #330<br>City Name, AB 10000<br>Phone : +1 555.010.4477<br>Fax : +1 555.010.4477<br>mail@example.com</p>
    </div>
    <div class="abs office" style="left:232px">
      <h4>Iriure Invidunt</h4>
      <p>2121 Sample Avenue #330<br>City Name, AB 10000<br>Phone : +1 555.010.4477<br>Fax : +1 555.010.4477<br>mail@example.com</p>
    </div>
    <div class="abs office" style="left:427px">
      <h4>Iriure Invidunt</h4>
      <p>2121 Sample Avenue #330<br>City Name, AB 10000<br>Phone : +1 555.010.4477<br>Fax : +1 555.010.4477<br>mail@example.com</p>
    </div>
    <div class="abs form">
      <h4>Contact Us</h4>
      <input style="margin-top:16px" value="Name" aria-label="Name">
      <input style="margin-top:10px" value="Email" aria-label="Email">
      <textarea style="margin-top:10px" aria-label="Message"></textarea>
      <div class="send">Send</div>
    </div>
    <h4 class="abs" style="left:37px;top:227px">We Accept</h4>
    <h4 class="abs" style="left:426px;top:227px">Follow Us</h4>
  </footer>

  <div class="abs badges" style="left:75px">
    <div class="badge b-light" style="width:58px">Carda</div>
    <div class="badge b-dark" style="width:59px">Carda Flash</div>
    <div class="badge b-light" style="width:58px">Paywell</div>
    <div class="badge b-dark" style="width:59px">Tallo</div>
    <div class="badge b-light" style="width:59px">Norvo</div>
  </div>
  <div class="abs social">
    <div class="s">Chirpa</div>
    <div class="s">Srch</div>
    <div class="s">Frendo</div>
    <div class="s">Feed</div>
  </div>

</div>
</body>
</html>
```